Vantor Ridge needs a Business Card Design

We need a business card design for an Information Technology company based in Fairfax Virginia called Vantor Ridge. We want the business card to use our logo colors. We need it to be double-sided. The business card needs to look professional but we would like it to be unique. You can get company information from our web site (http://www.vantorridgellc.example).

Target Market(s)

Target market is Government Agencies and Business Professionals.

Industry/Entity Type

Business

Requirements
Must have
• Must have section for company name, company address, company URL, employee name, title, phone and email. Also must have company logo and space for entering logos.

```html
<!DOCTYPE html>
<html lang="en">
<head>
<meta charset="utf-8">
<title>Vantor Ridge – Business Card</title>
<link href="https://fonts.googleapis.com/css2?family=Cinzel:wght@600&family=PT+Sans:wght@400;700&display=swap" rel="stylesheet">
<style>
  :root{
    --navy:#2b3990;
    --blue:#1a75bc;
    --grey-text:#6d6e71;
    --ink:#231f20;
    --frame:#333333;
    --card-edge:#b8b8b8;
    --badge-red:#e2231a;
    --badge-grey:#4d4d4d;
    --page:#ffffff;
  }
  *{margin:0;padding:0;box-sizing:border-box}
  html,body{width:1200px;height:927px;overflow:hidden;background:var(--page)}
  body{position:relative;font-family:"PT Sans",sans-serif;color:var(--ink)}
  .frame{position:absolute;top:270px;width:581px;height:350px;border:1.5px solid var(--frame)}
  .frame--front{left:12px}
  .frame--back{left:596px}
  .card{position:absolute;top:287px;height:311px;border:1.5px solid var(--card-edge);background:#fff;overflow:hidden}
  .card--front{left:30px;width:542px}
  .card--back{left:614px;width:541px}
  .abs{position:absolute}
  .wordmark{font-family:"Cinzel",serif;font-weight:600;color:var(--navy);white-space:nowrap;line-height:1}
  .mark-square{background:var(--navy)}
  .tagline{font-weight:700;color:var(--grey-text);letter-spacing:.2px;white-space:nowrap;line-height:1}
  .person-name{font-family:"Cinzel",serif;font-weight:600;white-space:nowrap;line-height:1}
  .designation{color:var(--grey-text);white-space:nowrap;line-height:1}

  /* front */
  .front-mark{left:50px;top:100px;width:57px;height:57px}
  .front-wordmark{left:122px;top:106px;font-size:44px}
  .front-tagline{left:126px;top:152px;font-size:13px}
  .front-name{left:22px;top:260px;font-size:32px;color:var(--navy)}
  .front-designation{left:23px;top:292px;font-size:15px}

  /* back */
  .partner-strip{left:0;top:0;width:59px;height:100%}
  .badge-bar{left:14px;top:8px;width:16px;height:128px;background:var(--badge-red)}
  .badge-bar--grey{top:150px;height:90px;background:var(--badge-grey)}
  .badge-square{left:10px;top:246px;width:32px;height:52px;background:var(--blue);border-radius:4px}
  .spine{left:59px;top:0;width:10px;height:100%;background:var(--blue)}
  .name-plate{left:266px;top:24px;width:275px;height:50px;display:flex}
  .name-plate__square{width:50px;height:50px;background:var(--navy)}
  .name-plate__bar{flex:1;background:var(--blue);display:flex;align-items:center;justify-content:flex-end;padding-right:15px}
  .back-name{font-size:26px;color:#fff}
  .back-designation{right:15px;top:79px;font-size:15px}
  .contact{right:15px;top:118px;text-align:right;font-size:14px;line-height:24px;color:var(--grey-text)}
  .contact b{color:var(--ink);font-weight:700}
  .contact .gap{display:inline-block;width:22px}
  .back-mark{left:76px;top:243px;width:50px;height:50px}
  .back-wordmark{left:140px;top:248px;font-size:29px}
  .back-tagline{left:143px;top:281px;font-size:10px}
  .corner-dark{left:436px;top:293px;width:18px;height:18px;background:var(--navy)}
  .corner-blue{left:454px;top:293px;width:87px;height:18px;background:var(--blue)}
</style>
</head>
<body>
  <div class="frame frame--front"></div>
  <div class="frame frame--back"></div>

  <section class="card card--front" aria-label="Card front">
    <div class="abs mark-square front-mark"></div>
    <div class="abs wordmark front-wordmark">Vantor Ridge</div>
    <div class="abs tagline front-tagline">TRANSFORMING IDEAS INTO SOLUTIONS</div>
    <div class="abs person-name front-name">Jordan Hale</div>
    <div class="abs designation front-designation">Company Designation</div>
  </section>

  <section class="card card--back" aria-label="Card back">
    <div class="abs partner-strip" aria-label="Partner badges">
      <div class="abs badge-bar"></div>
      <div class="abs badge-bar badge-bar--grey"></div>
      <div class="abs badge-square"></div>
    </div>
    <div class="abs spine"></div>

    <div class="abs name-plate">
      <div class="name-plate__square"></div>
      <div class="name-plate__bar"><span class="person-name back-name">Jordan Hale</span></div>
    </div>
    <div class="abs designation back-designation">Company Designation</div>

    <div class="abs contact">
      <div><b>Address:</b> 1450 Ledger Way, Suite 300 &nbsp;|&nbsp; Alder Crest, VA 20999</div>
      <div><b>Phone:</b> 877.555.0142<span class="gap"></span><b>Fax:</b> 888.555.0178</div>
      <div><b>Mail:</b> jordan.hale@vantorridgellc.example</div>
      <div><b>Web:</b> http://www.vantorridgellc.example</div>
    </div>

    <div class="abs mark-square back-mark"></div>
    <div class="abs wordmark back-wordmark">Vantor Ridge</div>
    <div class="abs tagline back-tagline">TRANSFORMING IDEAS INTO SOLUTIONS</div>

    <div class="abs corner-dark"></div>
    <div class="abs corner-blue"></div>
  </section>
</body>
</html>
```